Elegant wordpress web page for wedding rental of hand sanitizers

We want to rent our hand sanitizing towers out for high-end weddings. We need a very elegant, sophisticated page that describes our offering. You can see an ugly first draft here: trelvo.com/weddings
Target Market(s)
Wedding planners, wedding parents
Number of Pages Required
1 page
Font styles to use
Serif
Script
Colors
Designer to choose colors to be used in the design.
Requirements
Nice to have
- Two wedding-related sites for inspiration: quietorchardweddings-dot-com and fernlaneservices-dot-com

```html
<!DOCTYPE html>
<html lang="en">
<head>
<meta charset="utf-8">
<title>Trelvo Wedding Sanitizer</title>
<link rel="stylesheet" href="https://fonts.googleapis.com/css2?family=Saira+Condensed:wght@400;500;600&family=Saira+Semi+Condensed:wght@400&family=Bree+Serif&family=Open+Sans:wght@400;600&display=swap">
<style>
:root{
  --blue:#1b6a92;
  --blue-deep:#1a5f86;
  --ink:#222;
  --muted:#666;
  --light:#9ab9cc;
  --white:#fff;
  --foot:#efefef;
  --hero-a:#4d6b6e;
  --hero-b:#8a9a8a;
  --care-a:#3f7593;
  --care-b:#6a7a58;
}
*{margin:0;padding:0;box-sizing:border-box}
html,body{width:1200px;height:4000px;overflow:hidden;background:var(--white)}
body{position:relative;font-family:"Open Sans",sans-serif;color:var(--ink)}
.abs{position:absolute}
.cond{font-family:"Saira Condensed",sans-serif}
.photo{position:absolute}

/* hero */
.hero-photo{left:0;top:0;width:1200px;height:400px;background:linear-gradient(110deg,#3f5a4e 0%,#5d6d72 40%,#8a8e86 70%,#c9b7b4 100%)}
.hero-title{left:0;width:1200px;top:30px;text-align:center;color:var(--white);font-family:"Saira Condensed",sans-serif;font-weight:500;font-size:48px;line-height:84px;letter-spacing:1px}
.hero-rule{left:575px;top:211px;width:50px;height:1px;background:var(--white)}
.hero-sub{left:0;width:1200px;top:243px;text-align:center;color:var(--white);font-family:"Bree Serif",serif;font-size:19px;line-height:32px;letter-spacing:.5px}
.hero-btn{left:514px;top:337px;width:158px;height:54px;border:1px solid #ccc;background:rgba(255,255,255,.05);color:var(--white);font-size:11px;letter-spacing:1px;text-align:center;line-height:52px}

/* why */
.eyebrow{font-family:"Saira Condensed",sans-serif;font-size:12px;letter-spacing:1px;color:var(--ink)}
.why-title{left:113px;top:522px;font-family:"Saira Condensed",sans-serif;font-weight:500;font-size:66px;line-height:66px;color:var(--blue)}
.rule{height:1px;width:20px;background:var(--ink)}
.why-text{left:113px;top:690px;width:380px;font-family:"Saira Semi Condensed",sans-serif;font-size:14.5px;line-height:24px;color:var(--ink)}
.feature-title{font-family:"Saira Condensed",sans-serif;font-size:20px;line-height:25px;color:var(--blue)}
.feature-text{font-size:10px;line-height:16px;color:var(--muted);width:170px;margin-top:5px}
.feature-icon{position:absolute;width:50px;height:50px;fill:none;stroke:#333;stroke-width:1.6}

/* personalize */
.big-title{font-family:"Saira Condensed",sans-serif;font-weight:500;font-size:66px;line-height:74px;color:var(--blue)}
.bullets{left:624px;top:1296px;width:470px;font-size:12.5px;line-height:26px;letter-spacing:.3px;color:#444;list-style:none}
.bullets li{position:relative;padding-left:16px}
.bullets li::before{content:"";position:absolute;left:2px;top:11px;width:4px;height:4px;border-radius:50%;background:#444}
.line-link{font-size:11px;letter-spacing:.8px;color:var(--ink);border-top:1px solid var(--ink);padding-top:12px}

/* design */
.design-title{left:400px;width:400px;top:1730px;text-align:center;font-family:"Saira Condensed",sans-serif;font-weight:500;font-size:52px;line-height:66px;color:var(--blue)}
.design-text{left:450px;width:303px;top:1928px;text-align:center;font-size:13px;line-height:25.4px;letter-spacing:.3px;color:#444}
.outline-btn{left:562px;top:2167px;width:172px;height:51px;border:1px solid var(--blue);font-size:11px;letter-spacing:.8px;text-align:center;line-height:49px;color:var(--ink)}

/* testimonials */
.quote{width:306px;text-align:center;font-size:13px;line-height:25px;color:var(--ink)}
.quote-box{left:439px;top:2359px;width:306px;height:248px;background:var(--blue)}
.person{display:flex;align-items:center;gap:12px}
.avatar{width:60px;height:60px;border-radius:50%;background:linear-gradient(135deg,#c7b3a6,#6a5548)}
.p-name{font-family:"Saira Condensed",sans-serif;font-size:22px;line-height:24px;color:var(--blue)}
.p-role{font-size:11px;letter-spacing:.8px;color:var(--light)}

/* care */
.care-title{left:0;width:1200px;top:2870px;text-align:center;font-family:"Saira Condensed",sans-serif;font-weight:500;font-size:56px;color:var(--white)}
.care-item{width:310px;text-align:center;color:var(--white)}
.care-item h3{font-family:"Saira Condensed",sans-serif;font-weight:500;font-size:30px;line-height:36px;margin-bottom:10px}
.care-item p{font-family:Arial,sans-serif;font-size:13.5px;line-height:25px;color:#eef2f2}
.care-icon{display:block;margin:0 auto 8px;fill:none;stroke:var(--white);stroke-width:2}

/* footer */
.footer{left:0;top:3827px;width:1200px;height:173px;background:var(--foot)}
.foot-text{font-size:18px;line-height:33px;color:var(--ink)}
.social{width:30px;height:30px;background:var(--blue-deep)}
</style>
</head>
<body>

<!-- hero -->
<div class="photo hero-photo" role="img" aria-label="Bride and groom beside a photo sanitizer stand with a large white flower arrangement, outdoor wedding"></div>
<svg class="abs" style="left:0;top:300px" width="1200" height="100" viewBox="0 0 1200 100"><polygon points="0,6 593,100 1200,6 1200,100 0,100" fill="var(--white)"/></svg>
<h1 class="abs hero-title">CUSTOMIZED HAND SANITIZER<br>FOR WEDDING</h1>
<div class="abs hero-rule"></div>
<p class="abs hero-sub">The most mature, sophisticated &amp; reliable commercial hand<br>sanitizer dispenser on the market today.</p>
<div class="abs hero-btn">HIRE US TODAY</div>

<!-- why -->
<div class="abs eyebrow" style="left:113px;top:491px">WHY WE'RE THE BEST</div>
<h2 class="abs why-title">Trelvo Wedding<br>Sanitizer</h2>
<div class="abs rule" style="left:113px;top:680px"></div>
<p class="abs why-text">Including hand sanitizer in your wedding plans has never been easier. We know how to keep your guests safe, from personalized hand sanitizers, that are not only cost effective but attractive too.</p>

<svg class="feature-icon" style="left:568px;top:518px" viewBox="0 0 50 50"><rect x="3" y="6" width="36" height="26" rx="2"/><path d="M3 12h36M14 40h14M21 32v8"/><rect x="30" y="24" width="16" height="18"/><path d="M34 30h8M34 35h8"/></svg>
<div class="abs" style="left:630px;top:500px"><div class="feature-title">Customized<br>&amp; Generic</div><p class="feature-text">Lorem ipsum dolor sit amet, consectetur adipiscing elit. Ut elit tellus,</p></div>

<svg class="feature-icon" style="left:812px;top:520px" viewBox="0 0 50 50"><rect x="19" y="3" width="12" height="12"/><circle cx="25" cy="9" r="3"/><path d="M25 15v10M10 25h30M10 25v8M25 25v8M40 25v8"/><rect x="5" y="33" width="10" height="9"/><rect x="20" y="33" width="10" height="9"/><rect x="35" y="33" width="10" height="9"/></svg>
<div class="abs" style="left:874px;top:500px"><div class="feature-title">Attractive<br>&amp; Quality Based</div><p class="feature-text">Lorem ipsum dolor sit amet, consectetur adipiscing elit. Ut elit tellus,</p></div>

<svg class="feature-icon" style="left:568px;top:672px" viewBox="0 0 50 50"><rect x="4" y="8" width="12" height="30"/><rect x="19" y="4" width="12" height="34"/><rect x="34" y="8" width="12" height="30"/><path d="M10 38v8M25 38v8M40 38v8M7 16h6M22 12h6M37 16h6"/></svg>
<div class="abs" style="left:630px;top:640px"><div class="feature-title">Different<br>Standanrd<br>&amp; Design</div><p class="feature-text">Lorem ipsum dolor sit amet, consectetur adipiscing elit. Ut elit tellus,</p></div>

<svg class="feature-icon" style="left:812px;top:660px" viewBox="0 0 50 50"><path d="M25 3l5 4 6-1 2 6 6 3-2 6 3 5-5 4 0 6-6 1-4 5-5-3-6 2-3-6-6-2 1-6-4-5 4-5-1-6 6-2 3-6 6 2z"/><circle cx="25" cy="25" r="11"/><path d="M19 25l4 4 8-8"/></svg>
<div class="abs" style="left:874px;top:640px"><div class="feature-title">Cost-Effective<br>Rent</div><p class="feature-text">Lorem ipsum dolor sit amet, consectetur adipiscing elit. Ut elit tellus,</p></div>

<!-- personalize -->
<div class="photo" style="left:127px;top:947px;width:444px;height:572px;background:linear-gradient(160deg,#e8e4ea 0%,#d9d2d8 50%,#b9a7a7 80%,#6d5e58 100%)" role="img" aria-label="White wedding backdrop with flower arrangements and a photo sanitizer stand"></div>
<div class="photo" style="left:84px;top:1304px;width:208px;height:290px;background:linear-gradient(180deg,#8e8a86 0%,#c7c1bc 55%,#9f958c 100%);outline:3px solid var(--white)" role="img" aria-label="Sanitizer tower with a couple photo panel in a reception hall"></div>
<div class="abs eyebrow" style="left:624px;top:1061px">LOREM IPSUM DOLOR</div>
<h2 class="abs big-title" style="left:620px;top:1088px">Personalize your<br>Hand Sanitizer</h2>
<div class="abs rule" style="left:620px;top:1265px;width:26px"></div>
<ul class="abs bullets">
<li>Customize the photo above the spout and the spout decoration.</li>
<li>You can choose any size and shape photo you wish.</li>
<li>Choose from our standard spout decorations or design one of your own.&nbsp; We'll take care of producing and fitting it.</li>
</ul>
<div class="abs line-link" style="left:899px;top:1448px;width:184px">CHECK PRICE &amp; AVAILABLITY <span style="float:right">&#10230;</span></div>

<!-- design -->
<div class="photo" style="left:0;top:1689px;width:399px;height:582px;background:linear-gradient(180deg,#c2c2d0 0%,#d6d4dc 50%,#b8b7c6 100%)" role="img" aria-label="Sanitizer tower with a bride and groom photo panel"></div>
<div class="photo" style="left:801px;top:1689px;width:399px;height:582px;background:linear-gradient(180deg,#4d3a33 0%,#7c6a60 45%,#a99c95 100%)" role="img" aria-label="Sanitizer tower with couple photo in a rustic barn venue"></div>
<h2 class="abs design-title">GET YOUR OWN<br>DESIGN</h2>
<div class="abs rule" style="left:585px;top:1889px;width:30px"></div>
<p class="abs design-text">Once you've sourced your wedding sanitizer, work with our planner or designer to figure out how it should go and how it should be look. We suggest you some of best standard soup or you can tell us what is on your mind or else you send your own design to us.</p>
<div class="abs line-link" style="left:452px;top:2177px;width:96px">LEARN MORE <span style="float:right">&#9906;</span></div>
<div class="abs outline-btn">CHECK OPTIONS &nbsp;&#10230;</div>

<!-- testimonials -->
<div class="abs quote" style="left:106px;top:2383px">Click edit button to change this text. Lorem ipsum dolor sit amet, consectetur adipiscing elit. Ut elit tellus, luctus nec ullamcorper mattis, pulvinar dapibus leo.</div>
<div class="abs person" style="left:180px;top:2523px"><div class="avatar" role="img" aria-label="Portrait of Lena Harlow"></div><div><div class="p-name">Lena Harlow</div><div class="p-role">DESIGNER</div></div></div>

<div class="abs quote-box"></div>
<div class="abs quote" style="left:439px;top:2383px;color:var(--white)">Click edit button to change this text. Lorem ipsum dolor sit amet, consectetur adipiscing elit. Ut elit tellus, luctus nec ullamcorper mattis, pulvinar dapibus leo.</div>
<div class="abs person" style="left:514px;top:2523px"><div class="avatar" role="img" aria-label="Portrait of Mira Colton"></div><div><div class="p-name" style="color:var(--white)">Mira Colton</div><div class="p-role" style="color:#d6e4ec">DESIGNER</div></div></div>

<div class="abs quote" style="left:774px;top:2383px">Click edit button to change this text. Lorem ipsum dolor sit amet, consectetur adipiscing elit. Ut elit tellus, luctus nec ullamcorper mattis, pulvinar dapibus leo.</div>
<div class="abs person" style="left:858px;top:2523px"><div class="avatar" role="img" aria-label="Portrait of Owen Pryce"></div><div><div class="p-name">Owen Pryce</div><div class="p-role">DESIGNER</div></div></div>

<!-- care -->
<svg class="abs" style="left:0;top:2662px" width="1200" height="1120" viewBox="0 0 1200 1120" role="img" aria-label="Blurred wedding reception scene tinted blue and olive">
<defs><linearGradient id="careGrad" x1="0" y1="0" x2="0" y2="1"><stop offset="0" stop-color="var(--care-a)"/><stop offset=".55" stop-color="#587a78"/><stop offset="1" stop-color="var(--care-b)"/></linearGradient></defs>
<polygon points="0,0 593,104 1188,0 1200,0 1200,1040 593,1117 0,1040" fill="url(#careGrad)"/>
</svg>
<div class="abs" style="left:563px;top:2845px;width:60px;height:1px;background:var(--white)"></div>
<h2 class="abs care-title">GREET YOUR GUESTS WITH AN ACT OF CARE</h2>

<div class="abs care-item" style="left:104px;top:3002px">
<svg class="care-icon" width="64" height="40" viewBox="0 0 64 40"><path d="M2 12l12-6 10 4 8-4 10 2 10-4 10 6M14 6l-6 20 16 10 14-4 10-12M28 14l8 6 6-2"/></svg>
<h3>Feel Welcome</h3><p>Make your friends and family feel welcome and safe with a rugged, durable hand sanitizer from Trelvo.</p></div>

<div class="abs care-item" style="left:438px;top:3002px">
<svg class="care-icon" width="64" height="50" viewBox="0 0 64 50"><path d="M30 4c-4 6-4 10 0 10s4-4 0-10zM20 12c-3 5-3 8 0 8s3-3 0-8zM40 12c-3 5-3 8 0 8s3-3 0-8zM4 34h18l10 4h18l10-8M4 34v12h40l16-10"/></svg>
<h3>Touchless</h3><p>Our battery-powered dispensers are reliable, wireless, and touchless.</p></div>

<div class="abs care-item" style="left:772px;top:2985px">
<svg class="care-icon" width="64" height="84" viewBox="0 0 64 84"><path d="M22 40V12a5 5 0 0110 0v26M32 34a5 5 0 0110 0v6M42 38a5 5 0 0110 0v10c0 16-8 30-24 30S10 66 10 54l12-8M16 14a14 14 0 0122-10"/></svg>
<h3>Your Choice</h3><p>You can customized all the hand sanitizers as you want. You can add any pictures and shape on them.</p></div>

<div class="abs care-item" style="left:104px;top:3285px">
<svg class="care-icon" width="64" height="84" viewBox="0 0 64 84"><path d="M18 4h20v12H18zM14 26h28v54H14zM18 16l-4 10M38 16l4 10M20 44h16v22H20z"/><circle cx="52" cy="20" r="4"/><circle cx="56" cy="32" r="3"/></svg>
<h3>Pro Equipment</h3><p>All hand sanitizers that we provide are built with latest technology and specially for occasion like wedding.</p></div>

<div class="abs care-item" style="left:438px;top:3285px">
<svg class="care-icon" width="64" height="120" viewBox="0 0 64 120"><path d="M20 10c-10 10-8 30 4 34 10-4 10-24-4-34zM46 6c-12 6-14 24-4 30 10-4 12-20 4-30zM24 44c-2 30 6 50 14 70M42 36c0 30-4 50-4 78"/></svg>
<h3>According Theme</h3><p>The best thing about our sanitizers is that you can design our sanitizers according to your wedding theme.</p></div>

<div class="abs care-item" style="left:772px;top:3296px">
<svg class="care-icon" width="64" height="64" viewBox="0 0 64 64"><path d="M12 24a22 22 0 0138-8M52 40a22 22 0 01-38 8M50 6v10H40M14 58V48h10"/><circle cx="32" cy="32" r="6"/></svg>
<h3>Safe Feeling</h3><p>Our sanitizers will make your guest feel safe, so they can cheer and enjoy freely.</p></div>

<div class="abs line-link" style="left:502px;top:3626px;width:182px;color:var(--white);border-color:var(--white)">CHECK PRICE &amp; AVAILABLITY <span style="float:right">&#9906;</span></div>

<!-- footer -->
<div class="abs footer"></div>
<svg class="abs" style="left:180px;top:3878px" width="34" height="46" viewBox="0 0 34 46"><path d="M17 44C6 28 3 22 3 16a14 14 0 0128 0c0 6-3 12-14 28z" fill="none" stroke="#888" stroke-width="2"/><circle cx="17" cy="16" r="5" fill="none" stroke="#888" stroke-width="2"/></svg>
<div class="abs foot-text" style="left:248px;top:3858px">218 Alder Row<br>South<br>Millbrook, N.Y.</div>
<div class="abs social" style="left:520px;top:3898px"></div>
<div class="abs social" style="left:558px;top:3898px"></div>
<div class="abs social" style="left:596px;top:3898px"></div>
<div class="abs social" style="left:634px;top:3898px"></div>
<div class="abs foot-text" style="left:771px;top:3859px">info@trelvo.com</div>
<div class="abs foot-text" style="left:799px;top:3894px">555-214-7093</div>
<svg class="abs" style="left:980px;top:3872px" width="56" height="56" viewBox="0 0 56 56"><path d="M8 42L38 12l8 8-30 30H8zM34 16l8 8M8 42l8 8M6 54h44" fill="none" stroke="#999" stroke-width="2"/></svg>

</body>
</html>
```